Herbal tea shop web designing - Brewvine

We need a business-charity purpose online shop selling premium Brewvine with a tagline "Healthy with a heart" where all the raw materials are being purchased from Indonesian local farmers in order to give them sustainable employment. Every 20% from the total amount of the customer's purchase from our website always goes back to their communities to help build better sanitation, education or whatever they need. We need page to blog too and another page for customers to interact and share their thought. we expect an eye catching simple earthy (maybe a bit rustic) design with some brush lettering font in some parts. Thank you.

Target Market(s)

-Tea Lovers
-Anyone with body weight issues or any health issues in general

Industry/Entity Type

Home Health Care

Number of Pages Required

5+ page

Font styles to use
Other font styles liked:
• brush lettering font in some parts

Requirements
Must have
• - Brush lettering font
• -Simple, a bit rustic design with some nice watercolor touch
• -Blogging Page
• -catchy yet fancy and elegant E-commerce page
Nice to have
• Well, I will let the designers use their skills and imaginations to the fullest.

```html
<!DOCTYPE html>
<html lang="en">
<head>
<meta charset="utf-8">
<title>Brewvine – Our Blogs</title>
<link href="https://fonts.googleapis.com/css2?family=Roboto:wght@400;500;700&family=Kaushan+Script&display=swap" rel="stylesheet">
<style>
  :root{
    --white:#ffffff;
    --ink:#2b2b2b;
    --footer:#35302c;
    --footer-text:#d9d4cf;
    --footer-line:#4a4541;
    --accent:#1fa35a;
    --btn-border:#d8d8d8;
  }
  *{margin:0;padding:0;box-sizing:border-box}
  html,body{width:1032px;height:1200px;overflow:hidden;background:var(--white)}
  body{position:relative;font-family:"Roboto",Arial,sans-serif;color:var(--ink)}

  .hero{position:absolute;left:0;top:0;width:1032px;height:212px;
    background:linear-gradient(90deg,#6f655c 0%,#8a7a6b 30%,#9b7a5e 50%,#5d5550 75%,#3f3d3d 100%)}
  .hero-shade{position:absolute;inset:0;background:rgba(20,15,10,.35)}
  .nav{position:absolute;top:30px;left:76px;display:flex;gap:0}
  .nav a{position:absolute;color:var(--white);font-size:10px;font-weight:500;text-decoration:none;white-space:nowrap}
  .nav .active-bar{position:absolute;top:-30px;left:104px;width:30px;height:2px;background:var(--white)}
  .brand{position:absolute;top:27px;left:0;width:1032px;text-align:center;color:var(--white);font-size:16px;font-weight:700}
  .hero-title{position:absolute;top:90px;left:0;width:1032px;text-align:center;color:var(--white);
    font-family:"Kaushan Script",cursive;font-size:46px;line-height:1}
  .tools{position:absolute;top:29px;display:flex;align-items:center;gap:4px;color:var(--white);font-size:10px;font-weight:500}
  .tools svg{display:block}

  .post{position:absolute;overflow:hidden;color:var(--white)}
  .post-shade{position:absolute;inset:0;background:linear-gradient(180deg,rgba(0,0,0,.12) 0%,rgba(0,0,0,0) 40%,rgba(0,0,0,.35) 100%)}
  .post-tag{position:absolute;left:21px;top:16px;font-size:8.5px;font-weight:700;letter-spacing:.2px}
  .post-title{position:absolute;left:21px;bottom:20px;font-size:14px;font-weight:700}
  .post.large .post-title{font-size:16px;bottom:31px}
  .post-play{position:absolute;right:13px;top:19px}

  .load-more{position:absolute;left:465px;top:883px;width:103px;height:33px;border:1px solid var(--btn-border);
    border-radius:17px;font-size:10.5px;font-weight:500;display:flex;align-items:center;justify-content:center;color:var(--ink);background:var(--white)}

  .footer{position:absolute;left:0;top:950px;width:1032px;height:250px;background:var(--footer);color:var(--footer-text)}
  .f-col{position:absolute;top:45px}
  .f-col h3{font-size:14px;font-weight:400;color:var(--white);margin-bottom:10px}
  .f-col li{list-style:none;font-size:11px;line-height:19.2px}
  .f-col p{font-size:11px;line-height:19.2px}
  .pay{margin-top:8px;font-size:13px;font-weight:700;color:var(--white)}
  .social li{display:flex;align-items:center;gap:8px;line-height:23px}
  .social .dot{width:6px;height:6px;background:var(--white);border-radius:50%}
  .f-rule{position:absolute;left:76px;top:206px;width:880px;height:1px;background:var(--footer-line)}
  .copy{position:absolute;left:78px;top:222px;font-size:11px}
  .to-top{position:absolute;left:977px;top:189px;width:34px;height:34px;border-radius:50%;background:var(--accent);display:flex;align-items:center;justify-content:center}
</style>
</head>
<body>

<header class="hero">
  <div role="img" aria-label="Blurred café scene with a smiling woman on the phone" style="position:absolute;inset:0;background:radial-gradient(ellipse 180px 160px at 520px 110px,#b8917a 0%,rgba(140,110,90,0) 100%)"></div>
  <div class="hero-shade"></div>
  <nav class="nav">
    <span class="active-bar"></span>
    <a style="left:0">HOME</a>
    <a style="left:53px">SHOP</a>
    <a style="left:104px">BLOGS</a>
    <a style="left:160px">TESTIMONIALS</a>
  </nav>
  <div class="brand">Brewvine</div>
  <h1 class="hero-title">Our Blogs</h1>
  <div class="tools" style="left:805px">
    <svg width="13" height="12" viewBox="0 0 24 22"><path d="M12 21 3 12a5.5 5.5 0 0 1 9-6.5A5.5 5.5 0 0 1 21 12z" fill="none" stroke="#fff" stroke-width="2.4"/></svg>
    WISHLIST
    <svg width="6" height="4" viewBox="0 0 6 4"><path d="M0 0l3 3 3-3" fill="none" stroke="#fff"/></svg>
  </div>
  <div class="tools" style="left:893px">
    <svg width="12" height="13" viewBox="0 0 12 14"><path d="M1 4h10v9H1z M3.5 4V3a2.5 2.5 0 0 1 5 0v1" fill="none" stroke="#fff" stroke-width="1.3"/></svg>
    0 ITEMS
    <svg width="6" height="4" viewBox="0 0 6 4"><path d="M0 0l3 3 3-3" fill="none" stroke="#fff"/></svg>
  </div>
</header>

<main>
  <article class="post" style="left:77px;top:262px;width:285px;height:183px">
    <div role="img" aria-label="Rosemary sprigs with lemon slices on linen" style="position:absolute;inset:0;background:linear-gradient(160deg,#e6e2da 0%,#b9b7ae 45%,#5d6b4d 70%,#8c8d88 100%)"></div>
    <div class="post-shade"></div>
    <span class="post-tag">DATE HERE</span>
    <h2 class="post-title">Some blog heading goes here</h2>
  </article>
  <article class="post" style="left:374px;top:262px;width:285px;height:183px">
    <div role="img" aria-label="Steaming tea bowl on a wooden table with loose leaves" style="position:absolute;inset:0;background:linear-gradient(180deg,#5b3a1e 0%,#8a6035 35%,#6c5a40 60%,#7f786e 100%)"></div>
    <div class="post-shade"></div>
    <span class="post-tag">DATE HERE</span>
    <h2 class="post-title">Some blog heading goes here</h2>
  </article>
  <article class="post" style="left:670px;top:262px;width:285px;height:183px">
    <div role="img" aria-label="Cup of tea surrounded by roasted coffee beans" style="position:absolute;inset:0;background:linear-gradient(120deg,#3a2518 0%,#5a3a25 40%,#d9d3cc 65%,#6b4a32 100%)"></div>
    <div class="post-shade"></div>
    <span class="post-tag">DATE HERE</span>
    <h2 class="post-title">Some blog heading goes here</h2>
  </article>
  <article class="post large" style="left:77px;top:461px;width:581px;height:381px">
    <div role="img" aria-label="Tea bowls, white teapot, dried herbs and pumpkins on a wooden board" style="position:absolute;inset:0;background:linear-gradient(165deg,#8fb7b4 0%,#b7a27a 30%,#9a6a3c 55%,#b89373 75%,#d7d4cf 100%)"></div>
    <div class="post-shade"></div>
    <span class="post-tag">INTERVIEWS</span>
    <svg class="post-play" width="12" height="12" viewBox="0 0 12 12"><circle cx="6" cy="6" r="6" fill="#fff"/><path d="M4.6 3.5v5l4-2.5z" fill="#555"/></svg>
    <h2 class="post-title">Some blog heading goes here...</h2>
  </article>
  <article class="post" style="left:670px;top:461px;width:285px;height:182px">
    <div role="img" aria-label="Glass tea press with yellow roses in a café" style="position:absolute;inset:0;background:linear-gradient(135deg,#4a3f38 0%,#8b857a 40%,#c6b99a 60%,#3b332d 100%)"></div>
    <div class="post-shade"></div>
    <span class="post-tag">DATE HERE</span>
    <h2 class="post-title">Some blog heading goes here</h2>
  </article>
  <article class="post" style="left:670px;top:659px;width:285px;height:183px">
    <div role="img" aria-label="Glass cups of mint tea with fresh leaves" style="position:absolute;inset:0;background:linear-gradient(135deg,#4f8a35 0%,#8ca56a 40%,#b6ae7e 60%,#d9dbd2 100%)"></div>
    <div class="post-shade"></div>
    <span class="post-tag">DATE HERE</span>
    <h2 class="post-title">Some blog heading goes here</h2>
  </article>

  <div class="load-more">LOAD MORE</div>
</main>

<footer class="footer">
  <div class="f-col" style="left:76px">
    <h3>About Us</h3>
    <p>Lorem ipsum dolor sit amet, consectetuer adipiscing elit.<br>Aenean commodo ligula eget dolor aenean massa.<br>Cum sociis natoque penatibus .</p>
    <div class="pay">PayNest</div>
  </div>
  <div class="f-col" style="left:420px">
    <h3>Informations</h3>
    <ul><li>About us</li><li>Sitemap</li><li>Advanced Search</li><li>Orders and Returns</li><li>Contact</li></ul>
  </div>
  <div class="f-col" style="left:619px">
    <h3>My Account</h3>
    <ul><li>Log In</li><li>View Shopping Cart</li><li>My wish list</li><li>Track My Order</li><li>Help</li></ul>
  </div>
  <div class="f-col" style="left:808px;top:45px">
    <h3 style="margin-bottom:6px">Follow us</h3>
    <ul class="social">
      <li><span class="dot"></span>Circlebook</li>
      <li><span class="dot"></span>Chirpline</li>
      <li><span class="dot"></span>Plusone</li>
      <li><span class="dot"></span>Snapgram</li>
    </ul>
  </div>
  <div class="f-rule"></div>
  <div class="copy">© 2017, All Rights Reserved.</div>
  <div class="to-top">
    <svg width="10" height="12" viewBox="0 0 10 12"><path d="M5 11V1M1 5l4-4 4 4" fill="none" stroke="#fff" stroke-width="1.3"/></svg>
  </div>
</footer>

</body>
</html>
```